Sponsorship and registration document for Charity Golf Day 2022

The project requires 2 documents to be updated to look more graphically savvy and professionally presentable.
1. Charity golf day sponsorship document
2. One page registration document.
The text has been completed. Text not to be changed - just graphics.
New images would be preferred.
The logos have been provided.

Target Market(s)

Corporate Sponsors and Golf players

Requirements
Must have
• Golf Theme

```html
<!DOCTYPE html>
<html lang="en">
<head>
<meta charset="utf-8">
<title>Charity Golf Day – Sponsorship Proposal</title>
<link rel="stylesheet" href="https://fonts.googleapis.com/css2?family=EB+Garamond:ital,wght@0,400;0,500;0,600;1,400&family=Open+Sans:wght@600;700&display=swap">
<style>
  :root{
    --navy:#0d2a78;
    --navy-deep:#0a2466;
    --blue-head:#1c3f94;
    --green:#8cc63f;
    --green-deep:#3aa34a;
    --teal:#a8d3cc;
    --ink:#2a2a2a;
    --paper:#ffffff;
    --bg:#e4e3e0;
    --gold:#e7c48d;
  }
  *{box-sizing:border-box;margin:0;padding:0}
  html,body{width:1200px;height:900px;overflow:hidden;background:var(--bg)}
  body{position:relative;font-family:"EB Garamond",Georgia,serif;color:var(--ink)}

  .page{position:absolute;top:188px;width:370px;height:523px;background:var(--paper);overflow:hidden;box-shadow:0 2px 10px rgba(0,0,0,.08)}
  .page--letter{left:25px}
  .page--info{left:395px}
  .page--cover{left:805px}

  /* Letter page */
  .letter__bg{position:absolute;inset:0;width:100%;height:100%}
  .letter__body{position:absolute;left:30px;right:30px;top:34px;font-size:7.6px;line-height:1.42}
  .letter__title{font-size:15px;line-height:1.2;font-weight:500;color:var(--navy);margin-bottom:12px}
  .letter__body p{margin-bottom:8px}
  .letter__list{list-style:none;margin:-4px 0 8px 0}
  .letter__list li::before{content:"•";color:var(--navy);margin-right:5px}
  .signoff{margin-top:12px;line-height:1.35}
  .signature{display:block;height:20px}
  .letter__rule{position:absolute;left:30px;bottom:30px;width:140px;height:1px;background:#fff}

  /* Info page */
  .info__body{position:absolute;left:28px;right:26px;top:30px;font-size:7.4px;line-height:1.38}
  .info__head{font-size:13px;font-weight:500;color:var(--blue-head);margin:8px 0 3px}
  .info__head:first-child{margin-top:0}
  .info__list{list-style:none;margin-bottom:4px}
  .info__list li{padding-left:9px;position:relative}
  .info__list li::before{content:"•";position:absolute;left:0}
  .info__body p{margin:8px 0 0 10px}
  .info__rule{position:absolute;left:28px;right:26px;bottom:64px;height:1px;background:#b9b9b9}
  .info__band{position:absolute;left:0;right:0;bottom:0;height:46px;background:var(--navy)}
  .band__title{position:absolute;left:28px;top:12px;font-style:italic;font-size:15px;color:#fff}
  .band__sub{position:absolute;right:26px;top:14px;font-style:italic;font-size:14px;color:var(--green)}
  .info__folio{position:absolute;left:28px;bottom:52px;font-size:8px;display:flex;align-items:center;gap:6px;color:var(--ink)}
  .folio__club{font-size:5.5px;color:var(--navy)}

  /* Cover */
  .cover__title{position:absolute;left:34px;top:34px;font-size:40px;line-height:.88;font-weight:500;color:var(--navy);letter-spacing:.5px}
  .cover__date{position:absolute;left:34px;top:118px;font-family:"Open Sans",Arial,sans-serif;font-weight:700;font-size:14px;line-height:1.2;color:#1d1d1d}
  .cover__art{position:absolute;left:0;top:150px;width:370px;height:210px}
  .cover__tagline{position:absolute;left:34px;top:364px;width:300px}
  .tagline__title{font-size:19px;font-weight:500;color:#1d1d1d;line-height:1.15}
  .tagline__sub{font-size:9px;line-height:1.35;color:#333;margin-top:3px;width:240px}
  .cover__url{position:absolute;left:34px;top:430px;font-size:9px;color:#333}
  .cover__club{position:absolute;right:26px;top:452px;display:flex;align-items:center;gap:6px;font-size:12px;font-weight:600;color:var(--navy)}
  .club__dot{width:12px;height:12px;border-radius:50%;background:var(--gold)}
  .cover__band{position:absolute;left:0;right:0;bottom:0;height:26px;background:var(--navy)}
</style>
</head>
<body>

  <!-- Inside left: cover letter -->
  <section class="page page--letter">
    <svg class="letter__bg" viewBox="0 0 370 523" preserveAspectRatio="none" role="img" aria-label="Soft teal to green hexagon pattern background">
      <defs>
        <linearGradient id="letterFade" x1="0" y1="0" x2="0" y2="1">
          <stop offset="0" stop-color="#a9d6cf"/>
          <stop offset=".45" stop-color="#dbe9e4"/>
          <stop offset=".7" stop-color="#c7e3a6"/>
          <stop offset="1" stop-color="#8cc850"/>
        </linearGradient>
      </defs>
      <rect width="370" height="523" fill="url(#letterFade)"/>
    </svg>
    <div class="letter__body">
      <h2 class="letter__title">Join us for an exclusive day on the private Ashbury Golf Course, with all proceeds going to support Prostate Cancer Research, Awareness and Support.</h2>
      <p>The Civic Club of Eastvale will again be holding its Charity Golf Day with all proceeds used to support the Prostate Cancer Research, Awareness and Support Programs. The venue will be the prestigious Ashbury Golf Club on Friday 25 March 2022, with a shotgun start at 8.00 am.</p>
      <p>We have enclosed for your information a copy of our promotional sponsor packages that outline the event, sponsorship package options and inclusions.</p>
      <p>The format of the day involves:</p>
      <ul class="letter__list">
        <li>Player registration, refreshments and light breakfast from 7.00am</li>
        <li>Ambrose competition starting at 8.00am</li>
        <li>Two Course lunch and presentations in the club house from 12.30pm</li>
      </ul>
      <p>Your commitment to supporting health programs in our community is truly appreciated. With assistance from sponsors such as yourself, we will continue to see improvements in the support and treatment for men and their families with prostate cancer.</p>
      <p>We hope that you will consider supporting this worthwhile event that is open to any organisation or individual who wishes to enjoy the benefits of playing golf at the prestigious Ashbury Golf Club.</p>
      <p>For more information, please check the website (www.eastvaleclub.org/golf-day) or should you wish to discuss any aspect of the event, please contact me on 0400 555 123.</p>
      <div class="signoff">
        Yours sincerely
        <span class="signature" role="img" aria-label="Handwritten signature"></span>
        Helena Marsh<br>Convener<br>Co-President 2021 - 2022<br>Secretary 2021 - 2022<br>Civic Club of Eastvale
      </div>
    </div>
    <div class="letter__rule"></div>
  </section>

  <!-- Inside right: facts page -->
  <section class="page page--info">
    <div class="info__body">
      <h3 class="info__head">Why prostate cancer?</h3>
      <ul class="info__list">
        <li>Prostate cancer is the most diagnosed cancer in Australian men.</li>
        <li>Approximately 20,000 Australian men are diagnosed with prostate cancer each year.</li>
        <li>Over 200,000 Australian men are living with a diagnosis of prostate cancer.</li>
        <li>95% of Australian men diagnosed with prostate cancer survive for at least 5 years.</li>
        <li>Almost 3,500 Australian men die of prostate cancer each year.</li>
      </ul>
      <h3 class="info__head">Why are we asking you to be involved?</h3>
      <ul class="info__list">
        <li>Every day 54 Australian men will be told they have prostate cancer</li>
        <li>70% of research applications are unfunded</li>
        <li>1 in 6 men will suffer from prostate cancer</li>
        <li>9 families lose a loved one to prostate cancer every day</li>
        <li>Only 1 in 3 men have access to a specialist nurse</li>
      </ul>
      <h3 class="info__head">What this fundraising event can achieve</h3>
      <ul class="info__list">
        <li>$12,500 – Could provide funding for a researcher working for one month on a project to reduce side - effects post treatment.</li>
        <li>$30,000 – could provide funding for a senior scientist for three months working on a project to improve treatments for prostate cancer that has spread to the bones.</li>
        <li>$50,000 – could fund a project to improve early - diagnosis for men with a family history of prostate cancer.</li>
      </ul>
      <p>Proceeds from this event will be donated to Prostate Cancer Research Group at the Life Sciences Discovery Institute, Southgate University, to fund world leading, innovative research and to support men and their families affected by prostate cancer.</p>
      <p>Their innovative research program has a strong translational approach, involving lab-based studies with tissues donated by patients with prostate cancer. Their collaborative studies with clinicians and patient advocates address questions that are relevant to patient care. The findings have the potential to improve the management and outcomes of men with different stages of prostate cancer. Recent studies have informed international guidelines for diagnosis of prostate cancer and led to new clinical trials.</p>
      <p>For more information visit their website www.southgate.edu/discovery/prostate-research</p>
    </div>
    <div class="info__folio">00 <span class="folio__club">Civic Club of Eastvale</span></div>
    <div class="info__rule"></div>
    <div class="info__band">
      <span class="band__title">Charity Golf Day</span>
      <span class="band__sub">Sponsorship Proposal</span>
    </div>
  </section>

  <!-- Front cover -->
  <section class="page page--cover">
    <h1 class="cover__title">CHARITY<br>GOLF DAY</h1>
    <div class="cover__date">Friday 25 March 2022<br>Ashbury Golf Club</div>

    <svg class="cover__art" viewBox="0 0 370 210">
      <defs>
        <linearGradient id="hexFill" x1="0" y1="0" x2="1" y2="1">
          <stop offset="0" stop-color="#b5dc7a"/>
          <stop offset="1" stop-color="#2f9a55"/>
        </linearGradient>
        <radialGradient id="photoFill" cx=".55" cy=".3" r=".8">
          <stop offset="0" stop-color="#f3f0a8"/>
          <stop offset=".45" stop-color="#b9cf58"/>
          <stop offset="1" stop-color="#4c8a22"/>
        </radialGradient>
        <clipPath id="artClip"><rect width="370" height="210"/></clipPath>
      </defs>
      <g clip-path="url(#artClip)">
        <path d="M250 -10 L370 -10 L370 100 A100 100 0 0 0 250 18 Z" fill="url(#hexFill)" role="img" aria-label="Green hexagon pattern"/>
        <path d="M125 65 A145 145 0 0 1 270 -5 L270 36 A105 105 0 0 0 178 80 Z" fill="var(--green)"/>
        <circle cx="288" cy="112" r="92" fill="var(--navy)"/>
        <circle cx="288" cy="112" r="80" fill="url(#photoFill)" role="img" aria-label="Photo of a golf club and ball on the green at sunrise"/>
        <circle cx="196" cy="90" r="36" fill="#fff" stroke="#7a7a7a" stroke-width=".8" stroke-dasharray="1.5 2"/>
        <circle cx="196" cy="90" r="28" fill="var(--gold)" opacity=".55"/>
      </g>
    </svg>

    <div class="cover__tagline">
      <div class="tagline__title">Supporting Prostate Cancer Research</div>
      <div class="tagline__sub">Help us hit prostate cancer off the green and beat the most common cancer in Australian men.</div>
    </div>
    <div class="cover__url">www.eastvaleclub.org/golf-day</div>
    <div class="cover__club"><span>Civic Club of Eastvale</span><span class="club__dot"></span></div>
    <div class="cover__band"></div>
  </section>

</body>
</html>
```